Marlow Realty Real Estate Brokerage Recruiting Flyer

We are a real estate brokerage looking to hire more real estate agents. We need to list everything we have to offer as a company so real estate agents will join our company. this is our company website: www.Marlowrealty.example .

100% COMMISSION NO MONTHLY FEE
$450 Flat Transaction FEE

What We Offer:
24/7 Office Access
Free E & O Insurance for 1st Year
Free Online CE and PLE
Free 1,000 Business Cards
Free Professional Social Media Marketing
Free Printing, Scanning, and Copies
Free Buyer and Seller Presentation Packages
Free Filquay Cloud Based Document Management Access
Access to our Internal Brokerage Forum
Company Profit Sharing!
Private Offices Available to Rent

*Lead Generation Software with over 3,000 Leads
*10 Leads to Start
* Free Personal CRM and Website
*Restrictions and Rules apply

Company Address:
4817 Amberfield Road
Suite 512
Fairfax, VA 22194
Phone: 703-555-0147
email: info@marlowrealty.example

Target Market(s)

Real Estate Agents

Industry/Entity Type

Real Estate

Colors
0555a3
ffffff

Requirements
Must have
• 100% COMMISSION NO MONTHLY FEE
$450 Flat Transaction FEE

What We Offer:
24/7 Office Access
Free Online CE and PLE
Free 1,000 Business Cards
Company Profit Sharing!

*10 Leads to Start

Company Address:
4817 Amberfield Road
Suite 512
Fairfax, VA 22194
Phone: 703-555-0147

```html
<!DOCTYPE html>
<html lang="en">
<head>
<meta charset="utf-8">
<title>Marlow Realty – Agent Recruiting Flyer</title>
<link href="https://fonts.googleapis.com/css2?family=Arimo:ital,wght@0,400;0,700;1,400&family=Bebas+Neue&family=Barlow+Semi+Condensed:wght@500&family=Crimson+Text:ital@1&display=swap" rel="stylesheet">
<style>
  :root {
    --navy: #1f3a7a;
    --yellow: #fcc52e;
    --grey: #d9d9db;
    --white: #ffffff;
    --ink: #1b1b1b;
    --backdrop: #cfe4f8;
  }
  * { margin: 0; padding: 0; box-sizing: border-box; }
  html, body {
    width: 1200px; height: 1200px; overflow: hidden;
    background: var(--backdrop);
    font-family: "Arimo", Arial, sans-serif;
  }
  .flyer {
    position: absolute; left: 200px; top: 36px;
    width: 800px; height: 1128px;
    background: var(--white); overflow: hidden;
    box-shadow: 0 6px 24px rgba(20, 40, 80, 0.25);
  }
  .hero-photo {
    position: absolute; left: 0; top: 0; width: 800px; height: 303px;
    background: linear-gradient(180deg, #b9c7d6 0%, #8b9cb3 35%, #3f4f73 65%, #5b5648 100%);
  }
  .headline-band {
    position: absolute; left: 0; top: 303px; width: 800px; height: 181px;
    background: var(--navy);
  }
  .headline {
    position: absolute; left: 30px; top: 320px; width: 530px;
    font-family: "Bebas Neue", Impact, sans-serif; font-weight: 400;
    font-size: 82px; line-height: 74px; color: var(--yellow);
    text-align: center; letter-spacing: 0.5px;
  }
  .fee-bar {
    position: absolute; left: 0; top: 484px; width: 565px; height: 53px;
    background: var(--grey);
  }
  .fee-bar p {
    font-family: "Crimson Text", Georgia, serif; font-style: italic;
    font-size: 34px; line-height: 53px; color: var(--ink);
    text-align: center; padding-left: 10px;
  }
  .fee-rule {
    position: absolute; left: 0; top: 537px; width: 800px; height: 14px;
    background: var(--navy);
  }
  .offer-tab {
    position: absolute; left: 0; top: 561px; width: 239px; height: 40px;
    background: var(--yellow);
    font-family: "Barlow Semi Condensed", Arial, sans-serif; font-weight: 500;
    font-size: 24px; line-height: 40px; color: var(--ink);
    padding-left: 56px;
  }
  .offer-list {
    position: absolute; left: 46px; top: 610px; list-style: none;
    font-size: 16.6px; line-height: 20.5px; color: var(--ink);
  }
  .offer-list li { display: flex; align-items: center; gap: 6px; white-space: nowrap; }
  .offer-list svg { width: 14px; height: 14px; flex: none; }
  .fine-print {
    position: absolute; left: 0; top: 844px; width: 565px; height: 66px;
    background: var(--grey);
    font-size: 12px; line-height: 13px; font-style: italic; color: var(--ink);
    padding: 8px 0 0 68px;
  }
  .fine-print .indent-1 { padding-left: 12px; }
  .fine-print .indent-2 { padding-left: 14px; }
  .agent-photo {
    position: absolute; left: 565px; top: 271px; width: 235px; height: 639px;
    background: linear-gradient(180deg, #d9c49a 0%, #c8b07e 25%, #efe4da 55%, #1d1d22 80%, #2a2a30 100%);
  }
  .footer {
    position: absolute; left: 0; top: 910px; width: 800px; height: 218px;
    background: var(--navy); color: var(--white);
  }
  .brand {
    position: absolute; left: 70px; top: 88px;
    display: flex; align-items: center; gap: 14px;
    font-size: 40px; font-weight: 400; color: var(--white); letter-spacing: 1px;
  }
  .brand-mark { width: 22px; height: 22px; background: var(--white); }
  .contact {
    position: absolute; left: 410px; top: 38px; width: 360px;
    text-align: center; font-size: 20px; line-height: 25.5px; font-style: normal;
  }
  .contact .strong { font-weight: 700; }
  .licence {
    position: absolute; left: 410px; top: 155px; width: 360px; text-align: center;
    font-family: "Crimson Text", Georgia, serif; font-style: italic; font-size: 16px;
  }
</style>
</head>
<body>
  <main class="flyer">
    <div class="hero-photo" role="img" aria-label="Photo of a modern two-storey blue-grey house with lit windows and a double garage among evergreen trees at dusk"></div>

    <div class="headline-band"></div>
    <h1 class="headline">100% Commission<br>No Monthly Fee</h1>

    <div class="fee-bar"><p>$450 Flat Transaction FEE</p></div>
    <div class="fee-rule"></div>

    <h2 class="offer-tab">What We Offer:</h2>
    <ul class="offer-list">
      <li><svg viewBox="0 0 14 14"><circle cx="7" cy="7" r="7" fill="#1f3a7a"/><path d="M3.6 7.2l2.3 2.2 4.4-4.6" stroke="#fff" stroke-width="1.8" fill="none"/></svg>24/7 Office Access</li>
      <li><svg viewBox="0 0 14 14"><circle cx="7" cy="7" r="7" fill="#1f3a7a"/><path d="M3.6 7.2l2.3 2.2 4.4-4.6" stroke="#fff" stroke-width="1.8" fill="none"/></svg>Free E &amp; O Insurance for 1st Year</li>
      <li><svg viewBox="0 0 14 14"><circle cx="7" cy="7" r="7" fill="#1f3a7a"/><path d="M3.6 7.2l2.3 2.2 4.4-4.6" stroke="#fff" stroke-width="1.8" fill="none"/></svg>Free Online CE and PLE</li>
      <li><svg viewBox="0 0 14 14"><circle cx="7" cy="7" r="7" fill="#1f3a7a"/><path d="M3.6 7.2l2.3 2.2 4.4-4.6" stroke="#fff" stroke-width="1.8" fill="none"/></svg>Free 1,000 Business Cards</li>
      <li><svg viewBox="0 0 14 14"><circle cx="7" cy="7" r="7" fill="#1f3a7a"/><path d="M3.6 7.2l2.3 2.2 4.4-4.6" stroke="#fff" stroke-width="1.8" fill="none"/></svg>Free Professional Social Media Marketing</li>
      <li><svg viewBox="0 0 14 14"><circle cx="7" cy="7" r="7" fill="#1f3a7a"/><path d="M3.6 7.2l2.3 2.2 4.4-4.6" stroke="#fff" stroke-width="1.8" fill="none"/></svg>Free Printing, Scanning, and Copies</li>
      <li><svg viewBox="0 0 14 14"><circle cx="7" cy="7" r="7" fill="#1f3a7a"/><path d="M3.6 7.2l2.3 2.2 4.4-4.6" stroke="#fff" stroke-width="1.8" fill="none"/></svg>Free Buyer and Seller Presentation Packages</li>
      <li><svg viewBox="0 0 14 14"><circle cx="7" cy="7" r="7" fill="#1f3a7a"/><path d="M3.6 7.2l2.3 2.2 4.4-4.6" stroke="#fff" stroke-width="1.8" fill="none"/></svg>Free Filquay Cloud Based Document Management Access</li>
      <li><svg viewBox="0 0 14 14"><circle cx="7" cy="7" r="7" fill="#1f3a7a"/><path d="M3.6 7.2l2.3 2.2 4.4-4.6" stroke="#fff" stroke-width="1.8" fill="none"/></svg>Access to our Internal Brokerage Forum</li>
      <li><svg viewBox="0 0 14 14"><circle cx="7" cy="7" r="7" fill="#1f3a7a"/><path d="M3.6 7.2l2.3 2.2 4.4-4.6" stroke="#fff" stroke-width="1.8" fill="none"/></svg>Company Profit Sharing!</li>
      <li><svg viewBox="0 0 14 14"><circle cx="7" cy="7" r="7" fill="#1f3a7a"/><path d="M3.6 7.2l2.3 2.2 4.4-4.6" stroke="#fff" stroke-width="1.8" fill="none"/></svg>Private Offices Available to Rent</li>
    </ul>

    <div class="fine-print">
      <p>*Lead Generation Software with over 3,000 Leads</p>
      <p class="indent-1">*10 Leads to Start</p>
      <p class="indent-2">* Free Personal CRM and Website</p>
      <p>*Restrictions and Rules apply</p>
    </div>

    <div class="agent-photo" role="img" aria-label="Photo of a real estate agent in a black blazer holding a folder and a small model house"></div>

    <footer class="footer">
      <div class="brand"><span class="brand-mark"></span>Marlow Realty</div>
      <address class="contact">
        <p>4817 Amberfield Road</p>
        <p>Suite 512, Fairfax, VA 22194</p>
        <p class="strong">Phone: 703-555-0147</p>
        <p class="strong">Email: info@marlowrealty.example</p>
      </address>
      <p class="licence">Licensed in D.C., Maryland, and Virginia</p>
    </footer>
  </main>
</body>
</html>
```